Communication and Marketing agency needs a new presentation card

We are a group of communication and marketing agencies specialized in companies that are in the logistics and industrial sector. The head agency is TELVANO Grupo and the group consists of 4 agencies: TELVANO Media, TELVANO Digital, TELVANO Research and EnlazaPorImagen. We hace 4 offices in Spain (Madrid, Barcelona, Valencia and Murcia). We are looking for a clean and attractive design that transmits our experience, brand presence in the market and knowledge to those who receive the card.It has to maintain the colors of the logo that is attached.
Target Market(s)
logistics and industrial sector
Marketing department
Clean and attractive design

```html
<!DOCTYPE html>
<html lang="es">
<head>
<meta charset="utf-8">
<title>TELVANO Grupo – Tarjetas de presentación</title>
<link href="https://fonts.googleapis.com/css2?family=Open+Sans:wght@400;600;700&display=swap" rel="stylesheet">
<style>
  :root{
    --brand-red:#b3121f;
    --ink:#4a4a4a;
    --card:#ffffff;
    --stage:#e9eaec;
    --map-tone:#d9d9d9;
  }
  *{box-sizing:border-box;margin:0;padding:0}
  html,body{width:1200px;height:900px;overflow:hidden}
  body{
    background:var(--stage);
    font-family:"Open Sans",Arial,sans-serif;
    color:var(--ink);
    position:relative;
  }
  .card{
    position:absolute;
    left:260px;
    width:680px;height:410px;
    background:var(--card);
    border-radius:28px;
    box-shadow:0 6px 18px rgba(0,0,0,.12);
    overflow:hidden;
  }
  .card--contact{top:30px}
  .card--group{top:460px}

  /* Contact side */
  .person{position:absolute;left:48px;top:44px}
  .person__name{font-size:30px;font-weight:700;color:var(--ink)}
  .person__role{font-size:17px;font-weight:600;color:var(--brand-red);margin-top:2px}
  .person__rule{width:38px;height:3px;background:var(--brand-red);margin-top:12px}

  .contact-list{position:absolute;left:48px;top:236px;list-style:none}
  .contact-list li{display:flex;align-items:center;gap:10px;font-size:17px;color:var(--ink);height:30px}
  .contact-list svg{width:18px;height:18px;flex:none}

  .brand-name{font-weight:600;color:var(--brand-red);letter-spacing:1px;white-space:nowrap}
  .card--contact .brand-name{position:absolute;right:48px;top:118px;font-size:38px;line-height:1.1}

  .offices-map{
    position:absolute;right:70px;top:180px;
    width:220px;height:140px;
    border-radius:10px;
    background:radial-gradient(ellipse at 45% 45%,#cfcfcf 0%,var(--map-tone) 60%,#efefef 100%);
  }
  .offices{
    position:absolute;right:48px;top:330px;
    display:flex;gap:14px;list-style:none;
    font-size:13px;font-weight:700;color:var(--ink);
  }
  .web{font-weight:600;color:var(--brand-red);white-space:nowrap}
  .card--contact .web{position:absolute;right:48px;top:356px;font-size:24px;line-height:1.2}

  /* Group side */
  .group-brand{position:absolute;right:48px;top:110px;text-align:right}
  .group-brand .brand-name{font-size:52px;line-height:1.2}
  .group-brand .web{display:block;font-size:19px;margin-top:6px}

  .agency{position:absolute;font-size:19px;line-height:1.2}
  .agency--digital{left:44px;top:40px;color:var(--ink)}
  .agency--video{left:44px;top:210px;color:var(--brand-red);font-size:17px}
  .agency--media{left:260px;top:330px;color:var(--ink)}
  .agency--research{right:48px;top:330px;color:var(--ink)}
</style>
</head>
<body>

<section class="card card--contact" aria-label="Tarjeta de contacto">
  <div class="person">
    <h1 class="person__name">Lucía Berrocal</h1>
    <p class="person__role">Director</p>
    <div class="person__rule"></div>
  </div>

  <ul class="contact-list">
    <li>
      <svg viewBox="0 0 18 18" aria-hidden="true"><rect width="18" height="18" rx="3" fill="#b3121f"/><path d="M5 4h3l1 3-2 1a7 7 0 0 0 3 3l1-2 3 1v3c-5 0-9-4-9-9z" fill="#fff"/></svg>
      910 555 214
    </li>
    <li>
      <svg viewBox="0 0 18 18" aria-hidden="true"><rect x="5" y="2" width="8" height="14" rx="1.5" fill="none" stroke="#b3121f" stroke-width="1.6"/><circle cx="9" cy="13.5" r="0.9" fill="#b3121f"/></svg>
      600 555 387
    </li>
    <li>
      <svg viewBox="0 0 18 18" aria-hidden="true"><rect width="18" height="18" rx="3" fill="#b3121f"/><path d="M4 6h10v7H4z M4 6l5 4 5-4" fill="none" stroke="#fff" stroke-width="1.3"/></svg>
      lberrocal@telvano.es
    </li>
    <li>
      <svg viewBox="0 0 18 18" aria-hidden="true"><rect width="18" height="18" rx="3" fill="#b3121f"/></svg>
      luciaberrocal
    </li>
  </ul>

  <p class="brand-name">TELVANO Media</p>
  <div class="offices-map" role="img" aria-label="Mapa punteado de España con las oficinas marcadas en Madrid, Barcelona, Valencia y Murcia"></div>
  <ul class="offices">
    <li>Madrid</li><li>Barcelona</li><li>Valencia</li><li>Murcia</li>
  </ul>
  <p class="web">www.telvano.es</p>
</section>

<section class="card card--group" aria-label="Marcas del grupo">
  <p class="agency agency--digital brand-name">TELVANO Digital</p>
  <p class="agency agency--video brand-name">EnlazaPorImagen</p>
  <div class="group-brand">
    <p class="brand-name">TELVANO Grupo</p>
    <span class="web">www.telvano.es</span>
  </div>
  <p class="agency agency--media brand-name">TELVANO Media</p>
  <p class="agency agency--research brand-name">TELVANO Research</p>
</section>

</body>
</html>
```